Bill board design For Marlowe’s Construction

Billboard Design Request
Please design the billboard to match the branding, colors, and overall feel of our website: Marlowe's Construction Website
MARLOWE’S CONSTRUCTION
CONCRETE BUILT FOR GENERATIONS
⭐ 5-Star Rated on Zorvix
Please Include:
* All three attached project photos
* Company logo(s)
* Phone Number: 555-214-7630
* Website: MarlowesConstruction.example
* Zorvix logo with 5-star rating graphic
* Chatterly logo
* Pixtoria logo
Service Area:
Kalamazoo • Battle Creek • Coldwater • Grand Rapids
Please arrange the photos and layout in whatever way creates the strongest visual impact and readability from the road. The company name, headline, phone number, and website should be highly visible at highway speeds.
The overall appearance should be clean, professional, premium, and consistent with our website branding while highlighting our reputation, craftsmanship, and quality concrete work.
People Driving By
Concrete Construction

```html
<!DOCTYPE html>
<html lang="en">
<head>
<meta charset="utf-8">
<title>Marlowe’s Construction Billboard</title>
<link rel="stylesheet" href="https://fonts.googleapis.com/css2?family=Montserrat:wght@600;700;800&family=Oswald:wght@600&display=swap">
<style>
  :root {
    --brand-blue: #1e9ae6;
    --ink: #0a0a0a;
    --paper: #ffffff;
    --page: #f3f4f6;
    --star-gold: #f5b301;
    --photo-dark: #2b2a22;
    --photo-mid: #5d5a3a;
    --photo-warm: #8a4a32;
  }
  * { margin: 0; padding: 0; box-sizing: border-box; }
  html, body { width: 1064px; height: 1200px; overflow: hidden; background: var(--page); }
  body { position: relative; font-family: "Montserrat", sans-serif; }

  .billboard {
    position: absolute; left: 32px; top: 415px;
    width: 1000px; height: 369px;
    background: var(--ink);
    box-shadow: 0 14px 30px rgba(0,0,0,.35);
    overflow: hidden;
  }
  .billboard-shapes { position: absolute; inset: 0; width: 100%; height: 100%; }

  .text { position: absolute; white-space: nowrap; line-height: 1; }

  .headline { left: 421px; top: 14px; font-size: 88px; font-weight: 800; color: var(--brand-blue); letter-spacing: 0; }

  .tagline-row {
    position: absolute; left: 424px; top: 99px; width: 513px; height: 28px;
    display: flex; align-items: center; gap: 12px;
  }
  .tagline-rule { flex: 1; height: 3px; background: var(--brand-blue); }
  .tagline { font-size: 26px; font-weight: 700; color: var(--paper); white-space: nowrap; line-height: 1; }

  .service-title { left: 31px; top: 71px; font-size: 39px; font-weight: 700; color: var(--paper); }
  .service-list { position: absolute; left: 31px; top: 142px; list-style: none; }
  .service-list li { font-size: 26px; font-weight: 700; color: var(--ink); line-height: 33.5px; }
  .service-list li::before { content: "• "; font-size: 18px; vertical-align: 3px; }

  .rating-stars { left: 80px; top: 286px; font-size: 11px; color: var(--star-gold); letter-spacing: 1px; }
  .rating-name { left: 52px; top: 296px; font-size: 32px; font-weight: 700; color: var(--brand-blue); }
  .follow-pill {
    position: absolute; left: 46px; top: 337px; height: 15px; padding: 0 8px;
    border-radius: 8px; background: var(--brand-blue);
    font-size: 8px; font-weight: 700; color: var(--paper); line-height: 15px; white-space: nowrap;
  }

  .company-name { left: 359px; width: 182px; text-align: center; top: 322px; font-size: 25px; font-weight: 700; color: var(--paper); }
  .company-sub { left: 359px; width: 182px; text-align: center; top: 350px; font-size: 7px; font-weight: 700; color: var(--paper); letter-spacing: 4.5px; }

  .website { left: 698px; top: 283px; font-size: 16px; font-weight: 600; color: var(--paper); }
  .phone { left: 698px; top: 299px; font-family: "Oswald", sans-serif; font-size: 52px; font-weight: 600; color: var(--paper); letter-spacing: -0.5px; }
</style>
</head>
<body>
  <div class="billboard">
    <svg class="billboard-shapes" viewBox="0 0 1622 598" preserveAspectRatio="none">
      <defs>
        <linearGradient id="photoTone" x1="0" y1="0" x2="1" y2="0.3">
          <stop offset="0" stop-color="var(--photo-dark)"/>
          <stop offset="0.45" stop-color="var(--photo-mid)"/>
          <stop offset="0.85" stop-color="var(--photo-warm)"/>
          <stop offset="1" stop-color="var(--photo-dark)"/>
        </linearGradient>
        <linearGradient id="photoFade" x1="0" y1="0" x2="0" y2="1">
          <stop offset="0" stop-color="#0a0a0a" stop-opacity="0.85"/>
          <stop offset="0.2" stop-color="#0a0a0a" stop-opacity="0"/>
          <stop offset="0.7" stop-color="#0a0a0a" stop-opacity="0"/>
          <stop offset="1" stop-color="#0a0a0a" stop-opacity="1"/>
        </linearGradient>
      </defs>

      <g class="project-photo" role="img" aria-label="Photo of a crew pouring and finishing concrete in a residential yard">
        <rect x="655" y="200" width="965" height="300" fill="url(#photoTone)"/>
        <rect x="655" y="200" width="965" height="300" fill="url(#photoFade)"/>
      </g>

      <path class="info-panel" d="M0 0 H400 L640 252 Q678 298 640 346 L400 598 H0 Z" fill="var(--paper)"/>
      <polygon class="service-band" points="0,105 480,105 555,197 0,197" fill="var(--ink)"/>

      <path class="brand-triangle" d="M430 598 L702 343 Q727 320 752 343 L1012 598 Z" fill="var(--brand-blue)"/>

      <g class="phone-icon">
        <circle cx="1082" cy="535" r="36" fill="var(--paper)"/>
        <path d="M1068 515 l7 -3 l6 12 l-5 4 q4 9 12 13 l4 -5 l12 6 l-3 7 q-4 4 -10 2 q-22 -9 -27 -28 q-1 -6 4 -8 Z" fill="var(--brand-blue)"/>
      </g>
    </svg>

    <div class="text headline">CONCRETE</div>
    <div class="tagline-row">
      <span class="tagline-rule"></span>
      <span class="tagline">BUILT FOR GENERATIONS</span>
      <span class="tagline-rule"></span>
    </div>

    <div class="text service-title">Service Area</div>
    <ul class="service-list">
      <li>Kalamazoo</li>
      <li>Battle Creek</li>
      <li>Coldwater</li>
      <li>Grand Rapids</li>
    </ul>

    <div class="text rating-stars">★★★★★</div>
    <div class="text rating-name">Zorvix</div>
    <div class="follow-pill">FOLLOW US ON : Chatterly · Pixtoria</div>

    <div class="text company-name">MARLOWE’S</div>
    <div class="text company-sub">CONSTRUCTION LLC</div>

    <div class="text website">MarlowesConstruction.example</div>
    <div class="text phone">555-214-7630</div>
  </div>
</body>
</html>
```